Business cards for property management company

Need new business cards designed for our property management company and rental community, Amber Knoll Commons. These cards will be primarily picked up by rental applicants.

May be single or double sided design.

I need cards for two different people, listed below. The design can be the same for both, and the only information that will be different is name and email address.

Industry/Entity Type

Property Management

Requirements
Must have
• US standard business card - 2''x3.5'' horizontal design.

1. Logo (attached). The text does not have to stay below the logo, but the card does need to say "Amber Knoll Commons" somewhere on it (does not have to be same font as logo, but those fonts are Americana Extra Bold and BlackJack if needed).
2. Name: one with "Lena Halvorsen" and one with "Dorian Halvorsen"
3. Email address: one with "lena@amberknollhub.com" and one with "dorian@amberknollhub.com"
4. Web address: amberknollhub.com
5. Phone: 281.555.0182
6. Address: 7390 Whitlock Avenue, Dickinson, Texas 77512 (zip code may me omitted, at your discretion)
Should not have
• No rounded corners or special cuts.

No bevel, emboss or shadow effects.

As a note, please do not use our website as a basis for color or design schemes. We are working on a redesign, based around the new logo (attached to brief).

```html
<!DOCTYPE html>
<html lang="en">
<head>
<meta charset="utf-8">
<title>Amber Knoll Commons – Business Card</title>
<link rel="stylesheet" href="https://fonts.googleapis.com/css2?family=Alegreya:ital,wght@0,700;1,700&family=PT+Sans&display=swap">
<style>
  :root {
    --page-bg: #ece9e3;
    --card-light: #e5ebe7;
    --card-light-edge: #dbe3de;
    --leaf-green: #9aa83b;
    --leaf-green-deep: #87962f;
    --brand-green: #3e9a3f;
    --mark-tint: #cfe0cf;
    --name-ink: #4b4f36;
    --body-ink: #4a4a48;
    --icon-green: #8a9e3a;
    --faint-white: rgba(255, 255, 255, 0.28);
  }
  * { margin: 0; padding: 0; box-sizing: border-box; }
  html, body {
    width: 1200px;
    height: 784px;
    overflow: hidden;
    background: var(--page-bg);
  }
  .business-card {
    position: absolute;
    left: 60px;
    top: 80px;
    width: 1080px;
    height: 623px;
    display: flex;
    overflow: hidden;
  }
  .card-front {
    position: relative;
    width: 635px;
    height: 100%;
    background: linear-gradient(160deg, var(--card-light) 0%, var(--card-light-edge) 100%);
  }
  .brand-mark {
    position: absolute;
    left: 52px;
    top: 32px;
    width: 172px;
    height: 172px;
    border-radius: 50%;
    background: var(--mark-tint);
  }
  .card-leaf-panel {
    position: relative;
    flex: 1;
    height: 100%;
    background: radial-gradient(ellipse at 55% 40%, var(--leaf-green) 0%, var(--leaf-green-deep) 100%);
  }
  .panel-brand {
    position: absolute;
    left: 20px;
    top: 440px;
    font-family: "Alegreya", Georgia, serif;
    font-weight: 700;
    font-size: 36px;
    color: var(--faint-white);
    white-space: nowrap;
  }
  .person-name {
    position: absolute;
    left: 369px;
    top: 52px;
    font-family: "Alegreya", Georgia, serif;
    font-style: italic;
    font-weight: 700;
    font-size: 25px;
    color: var(--name-ink);
  }
  .company-name {
    position: absolute;
    left: 157px;
    top: 276px;
    font-family: "Alegreya", Georgia, serif;
    font-weight: 700;
    font-size: 37px;
    color: var(--brand-green);
    white-space: nowrap;
  }
  .contact-list {
    position: absolute;
    left: 80px;
    top: 331px;
    list-style: none;
    font-family: "PT Sans", Arial, sans-serif;
    font-size: 26px;
    color: var(--body-ink);
  }
  .contact-list li {
    position: relative;
    height: 41px;
    line-height: 36px;
    padding-left: 76px;
    white-space: nowrap;
  }
  .contact-icon {
    position: absolute;
    left: 4px;
    top: 5px;
    width: 26px;
    height: 26px;
  }
  .contact-icon * { fill: none; stroke: var(--icon-green); stroke-width: 2.2; }
  .contact-icon .solid { fill: var(--icon-green); stroke: none; }
</style>
</head>
<body>
  <div class="business-card">
    <section class="card-front">
      <div class="brand-mark" aria-hidden="true"></div>
      <p class="person-name">Dorian Halvorsen</p>
      <p class="company-name">Amber Knoll Commons</p>
      <ul class="contact-list">
        <li>
          <svg class="contact-icon" viewBox="0 0 26 26" aria-hidden="true">
            <circle cx="13" cy="13" r="11"/>
            <path class="solid" d="M9 7h3l1 4-2 1.5c.8 1.8 1.8 2.8 3.5 3.5L16 14l4 1v3c-6 .5-11.5-5-11-11z"/>
          </svg>
          281.555.0182
        </li>
        <li>
          <svg class="contact-icon" viewBox="0 0 26 26" aria-hidden="true">
            <rect x="2" y="5" width="22" height="16"/>
            <path d="M2 5l11 9 11-9"/>
          </svg>
          dorian@amberknollhub.com
        </li>
        <li>
          <svg class="contact-icon" viewBox="0 0 26 26" aria-hidden="true">
            <circle cx="13" cy="13" r="11"/>
            <ellipse cx="13" cy="13" rx="5" ry="11"/>
            <path d="M2 13h22M4 7h18M4 19h18"/>
          </svg>
          www.amberknollhub.com
        </li>
        <li>
          <svg class="contact-icon" viewBox="0 0 26 26" aria-hidden="true">
            <path class="solid" d="M13 2L1 13h4v11h6v-7h4v7h6V13h4z"/>
          </svg>
          7390 Whitlock Avenue,
        </li>
        <li>Dickinson, Texas 77512</li>
      </ul>
    </section>
    <div class="card-leaf-panel" role="img" aria-label="Close-up photograph of a green leaf showing its vein texture">
      <p class="panel-brand" aria-hidden="true">Amber Knoll Commons</p>
    </div>
  </div>
</body>
</html>
```